Business Cards for an 'affordable luxury' inner city home builder in Calgary.

We need a business card design that emulates the progressive, innovative, culture of our company and the modern style of our homes. Use our website www.velmarcrest-ab.com as a reference for the product we build.

Our company builds homes in the inner city space of Calgary, Alberta. We build affordable luxury.

Target Market(s)

Young professional Families

Contact Information for Business Card

Try to maintain consistency with the logo font and the card font.

Requirements
Must have
• The details must include: Name, education, title, phone number, website and email (Address is not as important)
• The design must be uniques (like our logo), elegant, sophisticated and modern.

```html
<!DOCTYPE html>
<html lang="en">
<head>
<meta charset="utf-8">
<title>Velmarcrest Homes Ltd — Business Card</title>
<link href="https://fonts.googleapis.com/css2?family=Montserrat:wght@400;500&display=swap" rel="stylesheet">
<style>
  :root {
    --backdrop: #0b0b0b;
    --card: #050505;
    --card-edge: #1a1a1a;
    --text-strong: #f2f2f2;
    --text-muted: #8a8a8a;
    --mark-grey: #bdbdbd;
    --mark-dim: #5e5e5e;
  }
  * { margin: 0; padding: 0; box-sizing: border-box; }
  html, body {
    width: 1200px;
    height: 900px;
    overflow: hidden;
    background: var(--backdrop);
    font-family: "Montserrat", sans-serif;
  }
  .stage {
    position: relative;
    width: 1200px;
    height: 900px;
  }
  .card {
    position: absolute;
    top: 150px;
    width: 340px;
    height: 595px;
    background: var(--card);
    border: 1px solid var(--card-edge);
    border-radius: 26px;
    box-shadow: 0 20px 50px rgba(0,0,0,0.7);
  }
  .card-front { left: 230px; }
  .card-back { left: 630px; }

  .identity {
    position: absolute;
    top: 110px;
    left: 0;
    width: 100%;
    text-align: center;
  }
  .person-name {
    color: var(--text-strong);
    font-size: 25px;
    font-weight: 400;
    letter-spacing: 1.5px;
  }
  .job-title {
    margin-top: 4px;
    color: var(--text-muted);
    font-size: 12px;
    letter-spacing: 2px;
  }
  .contact-icons {
    margin-top: 34px;
    display: flex;
    justify-content: center;
    align-items: center;
    gap: 12px;
    color: var(--text-muted);
  }
  .contact-icons .dash {
    width: 8px;
    height: 1px;
    background: var(--text-muted);
  }
  .contact-icons svg { width: 12px; height: 12px; }
  .contact-list {
    margin-top: 14px;
    list-style: none;
    color: var(--text-strong);
    font-size: 14px;
    line-height: 26px;
    letter-spacing: 0.5px;
  }

  .front-brand {
    position: absolute;
    left: 0;
    bottom: 80px;
    width: 100%;
    display: flex;
    flex-direction: column;
    align-items: center;
    gap: 16px;
  }
  .front-brand .brand-square {
    width: 46px;
    height: 46px;
    background: var(--mark-dim);
  }
  .front-brand .brand-name {
    color: var(--mark-grey);
    font-size: 20px;
    font-weight: 500;
    letter-spacing: 3px;
    text-transform: uppercase;
    text-align: center;
    line-height: 1.3;
  }

  .back-brand {
    position: absolute;
    top: 50%;
    left: 50%;
    transform: translate(-50%, -50%);
    display: flex;
    align-items: center;
    gap: 14px;
  }
  .back-brand .brand-square {
    width: 32px;
    height: 32px;
    background: var(--mark-dim);
  }
  .back-brand .brand-name {
    color: var(--mark-dim);
    font-size: 17px;
    font-weight: 500;
    letter-spacing: 2px;
    line-height: 1.2;
    text-transform: uppercase;
  }
</style>
</head>
<body>
<main class="stage">
  <section class="card card-front">
    <div class="identity">
      <h1 class="person-name">YOUR NAME</h1>
      <p class="job-title">JOB TITLE</p>
      <div class="contact-icons">
        <span class="dash"></span>
        <svg viewBox="0 0 24 24" aria-label="Phone"><path fill="currentColor" d="M6.6 10.8a15.1 15.1 0 0 0 6.6 6.6l2.2-2.2a1 1 0 0 1 1-.25 11.4 11.4 0 0 0 3.6.57 1 1 0 0 1 1 1V20a1 1 0 0 1-1 1A17 17 0 0 1 3 4a1 1 0 0 1 1-1h3.5a1 1 0 0 1 1 1c0 1.25.2 2.45.57 3.57a1 1 0 0 1-.25 1z"/></svg>
        <svg viewBox="0 0 24 24" aria-label="Email"><path fill="currentColor" d="M2 5h20v14H2z"/><path fill="none" stroke="#050505" stroke-width="2" d="M2 5l10 8 10-8"/></svg>
        <svg viewBox="0 0 24 24" aria-label="Website"><g fill="none" stroke="currentColor" stroke-width="2"><circle cx="12" cy="12" r="10"/><path d="M2 12h20M12 2c3 3 3 17 0 20M12 2c-3 3-3 17 0 20"/></g></svg>
        <span class="dash"></span>
      </div>
      <ul class="contact-list">
        <li>000 000 0000</li>
        <li>youremail@xyz.com</li>
        <li>www.yourwebsite.com</li>
      </ul>
    </div>
    <div class="front-brand">
      <span class="brand-square"></span>
      <p class="brand-name">Velmarcrest<br>Homes Ltd</p>
    </div>
  </section>

  <section class="card card-back">
    <div class="back-brand">
      <span class="brand-square"></span>
      <p class="brand-name">Velmarcrest<br>Homes<br>Ltd</p>
    </div>
  </section>
</main>
</body>
</html>
```